WORDPRESS WEB DESIGN PROJECT-DESIGN & DEVELOP

OUR BUSINESS
Bright Harbor Advisory provides effective project controls and management solutions for construction projects in Australia and Overseas. We provide services to both large multinational companies and smaller privately owned businesses. Our knowledge and expertise assist clients to effectively plan and manage their construction projects or project portfolios. Our focus is to provide your business with the tools, solutions and strategies necessary to deliver projects on time and within budget.

WHY WE ARE RE-BRANDING OUR WEBSITE
Our existing website design is not effective at promoting our business. We require a fresh, new, innovative approach to effectively market our business brand. Our new website will have the same look and feed as our newly developed business brochure.

DESIGN
Our new website will have the same look and feed as our business brochure. This website will be developed in Word press; a customized theme is required. The graphic design and images will enhance the written content; any graphics need to be developed in Photoshop as this is the software we use. A horizontal navigation menu will be implemented but must blend into the design and not be contained in a colour band. The webpage itself needs to span the entire viewable screen and must not look like an A4 piece of paper on a colored background. Additional design comments have been attached to this project as " website contents" word doc.

WEDSITES I LIKE THE LOOK OF
www.vantorelm.com (very professional, similar color scheme)
www.qurbikgear.com ( Good design, background made the website pop)
www.pelmorefloorwashing.com.au (clean,tidy,sharp images)
www.travelingua.com ( the look was simple but effective)
http://www.fendo-q.com

STYLE
We require a stylish, clean and easy to navigate website, with fresh, exciting and engaging imagery. Our website design needs to be modern, clean and sleek.

WRITTEN CONTENT
New written content for each page is provided with this project, there is 50% less content in this project than the original website.

QUALITY
High resolution images and photos will be used to promote an overall quality, professional look and feel.

FUNCTIONALITY
The design needs to be easily updated and editable. The person updating the webpage content and images does not know coding, so the theme will need to be able to interact with plugins. All design components need to be optimized for indexing on major search engines e.g. Firefox, internet explorer, Google and safari.

ICONS
I will require icon links to Email, Friendnest and LinkedIn, but not for twitter, Gmail or live feeds.

MENU
1.Home
2.Services
3.Benefits
4.Management
5.Planning
6.Optimization
7.Industry
8.Software
9.Contact us
10.Recruitment

TARGET AUDIENCE
Corporate Clients in all industry’s sectors
Supporting clients in
★OIL & Gas
★Iron Ore
★Coal
★New Industries
★Building and Construction
★Rail
★Civil
★Manufacturing
★Petrochemical
★Telecommunications

THE WINNER WILL PROVIDE
1. Wordpress theme with design.
2. List of plugins needed to meet requirements or design.
3. All images used in design.
4. Any custom php, javascript, or css files needed for the design.
5. List of core wordpress files customized as part of the design.
6. Any source files for custom images or design work (psd)

ATTACHMENTS
The following items will be attached to this project
1. Business logo
2. Icon images
3. Business Brochure PDF
4. Business brochure cover page psd file
5. Content required in each webpage

DESIGN AND DEVELOP
This project is to design and develop a word press website. In respect that the chosen designer may not be able to provide the development, 2 places of $400 each have been offered (1st for the design aspect, and 2nd for the development). The winning designer will receive $800 if both design and development have been achieved.

PROJECT CHANGES

The projects budget has increased from $600 to $800

Completion date has extended by 7 day.

• This design must have not appear out-dated or cluttered
Please do not provide any designs that look like our old website.

```html
<!DOCTYPE html>
<html lang="en">
<head>
<meta charset="utf-8">
<title>Bright Harbor Advisory</title>
<link href="https://fonts.googleapis.com/css2?family=PT+Sans:wght@400;700&family=PT+Sans+Narrow:wght@400;700&display=swap" rel="stylesheet">
<style>
:root{
  --red:#e8202a;
  --red-dark:#c51a22;
  --ink:#3a3b3f;
  --ink-dark:#2a2b2e;
  --text:#8a8a8a;
  --line:#d8d8d8;
  --white:#ffffff;
  --panel:#f4f4f4;
}
*{margin:0;padding:0;box-sizing:border-box}
html,body{width:1200px;height:823px;overflow:hidden;background:var(--white)}
body{font-family:"PT Sans",sans-serif;color:var(--text)}
.page{position:relative;width:1400px;height:960px;transform:scale(.857143);transform-origin:0 0;
  background:linear-gradient(#e6e6e6 0,#f7f7f7 40px,#fff 70px);}
.abs{position:absolute}

/* header */
.band{position:absolute;height:25px;background:var(--red)}
.band-dark{position:absolute;height:11px;background:var(--ink)}
.brand{position:absolute;left:790px;top:62px;width:285px;height:62px;display:flex;align-items:center;gap:10px}
.brand-mark{width:46px;height:46px;background:var(--red);flex:none}
.brand-text{display:flex;flex-direction:column}
.brand-name{font-family:"PT Sans",sans-serif;font-weight:700;font-size:21px;color:var(--ink-dark);line-height:1.05;text-transform:uppercase;letter-spacing:-.3px}
.brand-tag{font-size:8px;color:var(--ink);margin-top:3px}

/* nav */
.main-nav{position:absolute;left:210px;top:152px;width:708px;height:44px;
  background:linear-gradient(#5c5d61,#2f3034);border-radius:3px 3px 0 0;
  display:flex;justify-content:space-around;align-items:center;padding:0 6px}
.main-nav a{font-family:"PT Sans Narrow",sans-serif;color:var(--white);font-size:12.5px;text-decoration:none;text-transform:uppercase}

/* hero */
.hero{position:absolute;left:210px;top:196px;width:708px;height:291px;
  background:linear-gradient(160deg,#b6bcc2 0%,#7c8590 35%,#3e454d 70%,#22272c 100%)}
.hero-caption{position:absolute;left:0;top:159px;width:513px;height:116px;background:rgba(30,30,32,.72);padding:14px 25px}
.hero-title{font-size:34px;font-weight:400;color:var(--white);text-transform:uppercase;letter-spacing:-.3px;line-height:1.1}
.hero-sub{font-family:"PT Sans Narrow",sans-serif;font-size:13px;color:var(--white);text-transform:uppercase;line-height:20px;margin-top:10px}
.hero-arrows{position:absolute;right:8px;bottom:9px;display:flex;gap:4px}
.hero-arrows span{width:14px;height:14px;background:rgba(90,90,90,.7);display:block}

/* tiles */
.tile{position:absolute;width:169px;height:163px}
.tile-photo{width:100%;height:100%}
.tile-bar{position:absolute;left:0;bottom:0;width:100%;height:28px;display:flex}
.tile-label{flex:1;background:rgba(40,40,42,.85);color:var(--white);font-family:"PT Sans Narrow",sans-serif;font-size:12px;text-transform:uppercase;padding:7px 0 0 13px}
.tile-more{width:77px;background:var(--red-dark);color:var(--white);font-family:"PT Sans Narrow",sans-serif;font-size:10.5px;text-transform:uppercase;padding:8px 0 0 10px}

/* sidebar */
.welcome-head{position:absolute;left:943px;top:152px;width:247px;height:45px;
  background:linear-gradient(#5c5d61,#2f3034);border-radius:3px;
  color:var(--white);font-size:19px;text-align:center;line-height:45px;text-transform:uppercase}
.welcome-text{position:absolute;left:946px;top:210px;width:246px;font-size:12px;line-height:18px;color:var(--text)}
.welcome-text p+p{margin-top:18px}
.contact-box{position:absolute;left:943px;width:247px;height:59px;border:1px solid var(--line);
  background:linear-gradient(#fff,#f2f2f2);display:flex;align-items:center;padding-left:10px;gap:13px}
.contact-icon{width:40px;height:40px;background:linear-gradient(#555,#2b2b2b);border-radius:3px;display:flex;align-items:center;justify-content:center;flex:none}
.contact-title{color:var(--red);font-size:15px;text-transform:uppercase;line-height:18px}
.contact-sub{color:var(--ink);font-family:"PT Sans Narrow",sans-serif;font-size:11px;text-transform:uppercase;margin-top:3px}

/* footer */
.footer-rule{position:absolute;left:210px;top:860px;width:980px;height:2px;background:var(--line)}
.footer-nav{position:absolute;left:210px;top:884px;font-size:11px;color:#6b6b6b;display:flex}
.footer-nav span{padding:0 12px;border-left:1px solid #9a9a9a;line-height:12px}
.footer-nav span:first-child{padding-left:0;border-left:0}
.copyright{position:absolute;left:210px;top:907px;font-size:11px;color:#6b6b6b}
.footer-divider{position:absolute;left:940px;top:880px;width:1px;height:46px;background:var(--line)}
.footer-contact{position:absolute;left:963px;font-size:11px;color:#6b6b6b;display:flex;align-items:center;gap:8px}
</style>
</head>
<body>
<div class="page">

  <header>
    <div class="band" style="left:210px;top:71px;width:567px"></div>
    <div class="band-dark" style="left:210px;top:105px;width:567px"></div>
    <div class="band" style="left:1087px;top:71px;width:103px"></div>
    <div class="band-dark" style="left:1087px;top:105px;width:103px"></div>
    <div class="brand">
      <div class="brand-mark"></div>
      <div class="brand-text">
        <span class="brand-name">Bright Harbor Advisory</span>
        <span class="brand-tag">Providing Effective Project Controls and Management Solutions</span>
      </div>
    </div>
  </header>

  <nav class="main-nav">
    <a>Services</a><a>Benefits</a><a>Management</a><a>Planning</a><a>Optimization</a><a>Industry Software</a><a>Recruitment</a>
  </nav>

  <section class="hero" role="img" aria-label="Industrial refinery towers lit at dusk">
    <div class="hero-caption">
      <h1 class="hero-title">Bright Harbor Advisory</h1>
      <p class="hero-sub">Providing effective project controls and management solution to projects in Australia and overseas</p>
    </div>
    <div class="hero-arrows"><span></span><span></span></div>
  </section>

  <section class="tiles">
    <div class="tile" style="left:210px;top:498px"><div class="tile-photo" role="img" aria-label="Group of business professionals standing" style="background:linear-gradient(#e4e6ea,#9a9ea6)"></div><div class="tile-bar"><span class="tile-label">Services</span><span class="tile-more">Readmore »</span></div></div>
    <div class="tile" style="left:390px;top:498px"><div class="tile-photo" role="img" aria-label="Hands holding a green globe" style="background:linear-gradient(135deg,#f0f2ea,#7fb24a 55%,#3f7a25)"></div><div class="tile-bar"><span class="tile-label">Benifits</span><span class="tile-more">Readmore »</span></div></div>
    <div class="tile" style="left:570px;top:498px"><div class="tile-photo" role="img" aria-label="Two colleagues reviewing documents" style="background:linear-gradient(135deg,#e8e8e8,#9a8f86 55%,#4a4d52)"></div><div class="tile-bar"><span class="tile-label">Management</span><span class="tile-more">Readmore »</span></div></div>
    <div class="tile" style="left:750px;top:498px"><div class="tile-photo" role="img" aria-label="Team planning around a laptop" style="background:linear-gradient(135deg,#d9dde2,#7e848c 55%,#3a3e44)"></div><div class="tile-bar"><span class="tile-label">Planning</span><span class="tile-more">Readmore »</span></div></div>
    <div class="tile" style="left:210px;top:672px"><div class="tile-photo" role="img" aria-label="Businessmen assembling large puzzle pieces" style="background:linear-gradient(135deg,#f4f4f4,#c9cbce 55%,#6a6d72)"></div><div class="tile-bar"><span class="tile-label">Optimisation</span><span class="tile-more">Readmore »</span></div></div>
    <div class="tile" style="left:390px;top:672px"><div class="tile-photo" role="img" aria-label="Industrial pipework against blue sky" style="background:linear-gradient(135deg,#2f5f9a,#8a7f66 55%,#3c3a34)"></div><div class="tile-bar"><span class="tile-label">Industry</span><span class="tile-more">Readmore »</span></div></div>
    <div class="tile" style="left:570px;top:672px"><div class="tile-photo" role="img" aria-label="Man touching a digital network screen" style="background:linear-gradient(135deg,#dfe3e8,#8e959e 55%,#2c2f34)"></div><div class="tile-bar"><span class="tile-label">Software</span><span class="tile-more">Readmore »</span></div></div>
    <div class="tile" style="left:750px;top:672px"><div class="tile-photo" role="img" aria-label="Connected network of figures on blue lines" style="background:linear-gradient(135deg,#f2f2f2,#9fb4d6 55%,#3a66b0)"></div><div class="tile-bar"><span class="tile-label">Recruitment</span><span class="tile-more">Readmore »</span></div></div>
  </section>

  <aside>
    <h2 class="welcome-head" style="font-weight:400">Welcome</h2>
    <div class="welcome-text">
      <p>Bright Harbor Advisory provides effective project controls and management solutions for construction projects in Australia and Overseas. We provide services to both large multinational companies and smaller privately owned businesses. Our knowledge and expertise assist clients to effectively plan and manage their construction projects or project portfolios. Our focus is to provide your business with the tools, solutions and strategies necessary to deliver projects on time and within budget. We provide short or long term support, depending on your needs</p>
      <p>Many desktop publishing packages and web page editors now use Lorem Ipsum as their default model text, and a search for 'lorem ipsum' will uncover many web sites still in their infancy. Various versions have evolved over the years, sometimes by accident.default model text, and a search for 'lorem ipsum' will uncover many web sites still in their infancy.</p>
    </div>

    <div class="contact-box" style="top:628px">
      <div class="contact-icon"><svg width="26" height="20" viewBox="0 0 26 20"><rect x="1" y="1" width="24" height="18" fill="none" stroke="#fff" stroke-width="1.6"/><path d="M1 1l12 10 12-10M1 19l9-8M25 19l-9-8" fill="none" stroke="#fff" stroke-width="1.6"/></svg></div>
      <div><div class="contact-title">Email Us</div><div class="contact-sub">Click here</div></div>
    </div>
    <div class="contact-box" style="top:698px">
      <div class="contact-icon"><svg width="24" height="22" viewBox="0 0 24 22"><path d="M2 2h20v13H10l-5 5v-5H2z" fill="none" stroke="#fff" stroke-width="1.8" stroke-linejoin="round"/></svg></div>
      <div><div class="contact-title">Friendnest</div><div class="contact-sub">Follow us on</div></div>
    </div>
    <div class="contact-box" style="top:768px">
      <div class="contact-icon" style="background:none"><svg width="36" height="34" viewBox="0 0 36 34"><path d="M5 20v-4a13 13 0 0 1 26 0v4" fill="none" stroke="#555" stroke-width="3"/><rect x="2" y="18" width="8" height="12" rx="2" fill="#444"/><rect x="26" y="18" width="8" height="12" rx="2" fill="#444"/></svg></div>
      <div><div class="contact-title">Support Center</div><div class="contact-sub">Click here</div></div>
    </div>
  </aside>

  <footer>
    <div class="footer-rule"></div>
    <div class="footer-nav"><span>Home</span><span>Services</span><span>Benefits</span><span>Management</span><span>Planning</span><span>Optimization</span><span>Industry Software</span><span>Recruitment</span></div>
    <div class="copyright">Copyrights © 2013. Bright Harbor Advisory. All rights Reserved.</div>
    <div class="footer-divider"></div>
    <div class="footer-contact" style="top:882px"><svg width="13" height="13" viewBox="0 0 13 13"><path d="M3 1l2 3-1.5 1.5a7 7 0 0 0 4 4L9 8l3 2-1.5 2.5C5 12 1 8 .5 2.5z" fill="#8a8a8a"/></svg><span>+61 0400 555 018</span></div>
    <div class="footer-contact" style="top:904px"><svg width="13" height="10" viewBox="0 0 13 10"><rect width="13" height="10" fill="#8a8a8a"/><path d="M0 0l6.5 5L13 0" fill="none" stroke="#fff" stroke-width="1"/></svg><span>hello@brightharboradvisory.com.au</span></div>
  </footer>

</div>
</body>
</html>
```